Creating a visual for the various stage of our Packets by Locations: *Memphis Region *Clinics in TVR School District*Nashville Region *Knoxville Region. The attached file contains two tabs the layout of the packet scheme that currently in place and a second tab with the definition of the various cells that is needed as a legend on each report. The goal is to get the report tab an easily "eye" visual for the CEO of the company to follow. Create a Reporting Dashboard Template that we can input number into easily to update. The color scheme should reflect our website www.brightsprout.net
Target Market(s)
Pediatric company that performs Bright Sprout Exams and Optometry exams in school districts
Industry/Entity Type
Healthcare
Requirements
Must have
- Printable dash page. You can use this file and add a dash page that flows from the report page as an option in excel
Nice to have
- maybe 3D modern feel with the color scheme of the company website

```html
<!DOCTYPE html>
<html lang="en">
<head>
<meta charset="utf-8">
<title>Bright Sprout – Packet Dashboard</title>
<link href="https://fonts.googleapis.com/css2?family=Carlito:ital,wght@0,400;0,700;1,400&display=swap" rel="stylesheet">
<style>
:root{
  --bg:#ecebe8;
  --page:#ffffff;
  --band:#d3d3d3;
  --tab:#5b9bd5;
  --navy:#2f5597;
  --blue:#4472c4;
  --light:#9dc3e6;
  --pale:#b4c7e7;
  --row:#d9d9d9;
  --ink:#222;
  --muted:#595959;
}
*{margin:0;padding:0;box-sizing:border-box}
html,body{width:1200px;height:1000px;overflow:hidden;background:var(--bg);font-family:"Carlito",Calibri,Arial,sans-serif;color:var(--ink)}
.page{position:absolute;top:122px;width:533px;height:750px;background:var(--page);box-shadow:0 3px 12px rgba(0,0,0,.25)}
.page--report{left:47px}
.page--legend{left:621px}
.page__topband{position:absolute;left:0;top:0;width:100%;height:36px;background:var(--band)}
.page__footband{position:absolute;left:0;bottom:0;width:100%;height:26px;background:var(--band)}
.brand{position:absolute;left:30px;top:40px;display:flex;align-items:center;gap:8px}
.brand__mark{width:20px;height:20px;background:var(--navy)}
.brand__name{font-weight:700;font-size:30px;color:var(--navy);letter-spacing:-.5px}
.page__tab{position:absolute;right:0;top:46px;width:290px;height:37px;background:var(--tab);clip-path:polygon(22px 0,100% 0,100% 100%,0 100%);color:#fff;font-size:17px;display:flex;align-items:center;justify-content:center;padding-left:18px}
.charts{position:absolute;left:0;top:0}
.legend-table{position:absolute;left:44px;top:100px;width:446px;font-size:9.2px;line-height:11.2px}
.step{display:flex;background:var(--light);font-weight:700;margin-bottom:2px;padding:3px 0}
.step__num{width:30px;flex:none;text-align:center;font-size:13px;line-height:16px}
.step__text{padding-right:8px;align-self:center}
.cell{background:var(--row);padding:2px 8px 2px 32px;margin-bottom:2px}
.cell--italic{font-style:italic}
</style>
</head>
<body>

<section class="page page--report">
  <div class="page__topband"></div>
  <div class="brand"><span class="brand__mark"></span><span class="brand__name">Bright Sprout</span></div>
  <div class="page__tab">Nashville / Knoxville</div>
  <svg class="charts" width="533" height="750" viewBox="47 122 533 750" font-family="Carlito, Calibri, sans-serif">
    <defs>
      <linearGradient id="barGrad" x1="0" y1="0" x2="0" y2="1">
        <stop offset="0" stop-color="#6f95d8"/><stop offset="1" stop-color="#2f5597"/>
      </linearGradient>
      <linearGradient id="colGrad" x1="0" y1="0" x2="1" y2="0">
        <stop offset="0" stop-color="#3b63b0"/><stop offset="1" stop-color="#2a4d8f"/>
      </linearGradient>
    </defs>
    <text x="314" y="239" text-anchor="middle" font-size="13" font-weight="700" fill="#333">CX SYSTEM vs. PACKET TRACKING SYSTEM</text>
    <g stroke="#d9d9d9" stroke-width=".7">
      <line x1="180" y1="262" x2="180" y2="385"/><line x1="246" y1="262" x2="246" y2="385"/><line x1="312" y1="262" x2="312" y2="385"/>
      <line x1="378" y1="262" x2="378" y2="385"/><line x1="444" y1="262" x2="444" y2="385"/><line x1="510" y1="262" x2="510" y2="385"/>
      <line x1="180" y1="385" x2="510" y2="385"/>
    </g>
    <g font-size="7.5" fill="#333" text-anchor="end">
      <text x="173" y="276">Blanks Packets</text><text x="173" y="293">Decline Packets</text><text x="173" y="310">No Signature Packets</text>
      <text x="173" y="327">Incomplete Packets</text><text x="173" y="344">Duplicates Packets</text><text x="173" y="361">Complete Packets</text><text x="173" y="378">Call Center Packets</text>
    </g>
    <g fill="url(#barGrad)">
      <rect x="181" y="269" width="7" height="8" rx="2"/><rect x="181" y="286" width="14" height="8" rx="2"/>
      <rect x="181" y="320" width="12" height="8" rx="2"/><rect x="181" y="337" width="6" height="8" rx="2"/>
      <rect x="181" y="354" width="296" height="8" rx="2"/><rect x="181" y="371" width="2" height="8" rx="1"/>
    </g>
    <g font-size="8" fill="#333">
      <text x="193" y="276">489</text><text x="200" y="293">1034</text><text x="198" y="327">919</text>
      <text x="192" y="344">468</text><text x="482" y="361">22454</text><text x="188" y="378">49</text>
    </g>
    <g font-size="8" fill="#333" text-anchor="middle">
      <text x="180" y="397">0</text><text x="246" y="397">5000</text><text x="312" y="397">10000</text>
      <text x="378" y="397">15000</text><text x="444" y="397">20000</text><text x="510" y="397">25000</text>
      <text x="345" y="409" font-weight="700" font-size="7.5">Packets</text>
    </g>
    <line x1="100" y1="423" x2="525" y2="423" stroke="#9dc3e6"/>

    <text x="203" y="445" text-anchor="middle" font-size="10.5" font-weight="700" fill="#222">TOTAL PACKETS</text>
    <text x="432" y="442" text-anchor="middle" font-size="10.5" font-weight="700" fill="#222">INSURED &amp; UNINSURED PACKETS</text>

    <g>
      <ellipse cx="200" cy="538" rx="76" ry="46" fill="#1f3d72"/>
      <rect x="124" y="520" width="152" height="18" fill="#1f3d72"/>
      <path d="M200,520 L200,474 A76,46 0 1,1 162,480 Z" fill="#2f5597"/>
      <path d="M200,520 L162,480 A76,46 0 0,1 200,474 Z" fill="#8faadc"/>
      <text x="176" y="495" font-size="10" fill="#fff">2064</text>
      <text x="210" y="551" font-size="10" fill="#fff">23349</text>
    </g>
    <g>
      <ellipse cx="428" cy="538" rx="76" ry="46" fill="#7a9cc9"/>
      <rect x="352" y="520" width="152" height="18" fill="#7a9cc9"/>
      <path d="M428,520 L503,524 A76,46 0 1,1 428,474 Z" fill="#9dc3e6"/>
      <g transform="translate(6,-5)">
        <path d="M428,520 L503,524 L503,540 L428,536 Z" fill="#2a4d8f"/>
        <path d="M428,520 L428,474 A76,46 0 0,1 503,524 Z" fill="#4a78b8"/>
      </g>
      <text x="449" y="497" font-size="10" fill="#fff">5944</text>
      <text x="372" y="538" font-size="10" fill="#fff">16510</text>
    </g>
    <g font-size="7.5" fill="#333">
      <rect x="99" y="602" width="5" height="5" fill="#2f5597"/><text x="108" y="607">Packets Tracking System</text>
      <rect x="203" y="602" width="5" height="5" fill="#8faadc"/><text x="212" y="607">(Over)/Under Estimated</text>
      <rect x="361" y="602" width="5" height="5" fill="#4a78b8"/><text x="370" y="607">Uninsured Packets</text>
      <rect x="438" y="602" width="5" height="5" fill="#9dc3e6"/><text x="447" y="607">Insured Packets</text>
    </g>
    <line x1="100" y1="635" x2="525" y2="635" stroke="#9dc3e6"/>

    <text x="318" y="656" text-anchor="middle" font-size="13" font-weight="700" fill="#333">Comparison</text>
    <g stroke="#e0e0e0" stroke-width=".7">
      <line x1="240" y1="805" x2="255" y2="795"/><line x1="255" y1="795" x2="400" y2="795"/>
      <line x1="255" y1="772" x2="400" y2="772"/><line x1="255" y1="750" x2="400" y2="750"/>
      <line x1="255" y1="727" x2="400" y2="727"/><line x1="255" y1="705" x2="400" y2="705"/>
      <line x1="255" y1="682" x2="400" y2="682"/><line x1="255" y1="682" x2="255" y2="795"/>
      <line x1="240" y1="805" x2="385" y2="805"/>
    </g>
    <g font-size="7.5" fill="#333" text-anchor="end">
      <text x="232" y="808">0</text><text x="232" y="785">5000</text><text x="232" y="763">10000</text>
      <text x="232" y="740">15000</text><text x="232" y="718">20000</text><text x="232" y="695">25000</text>
    </g>
    <g>
      <polygon points="268,700 300,700 312,690 280,690" fill="#5b82c9"/>
      <polygon points="300,700 312,690 312,790 300,800" fill="#1f3d72"/>
      <rect x="268" y="700" width="32" height="100" fill="url(#colGrad)"/>
      <polygon points="346,726 378,726 390,716 358,716" fill="#5b82c9"/>
      <polygon points="378,726 390,716 390,790 378,800" fill="#1f3d72"/>
      <rect x="346" y="726" width="32" height="74" fill="url(#colGrad)"/>
      <polyline points="290,695 310,684 318,684" fill="none" stroke="#666" stroke-width=".6"/>
      <polyline points="368,721 382,712 388,712" fill="none" stroke="#666" stroke-width=".6"/>
      <text x="320" y="687" font-size="8" fill="#333">22354</text>
      <text x="390" y="715" font-size="8" fill="#333">16510</text>
      <text x="276" y="820" font-size="8" fill="#333">2017-18</text>
      <text x="354" y="820" font-size="8" fill="#333">2018-19</text>
    </g>
  </svg>
  <div class="page__footband"></div>
</section>

<section class="page page--legend">
  <div class="page__topband"></div>
  <div class="brand"><span class="brand__mark"></span><span class="brand__name">Bright Sprout</span></div>
  <div class="page__tab">Definitions of stages for a packet</div>
  <div class="legend-table">
    <div class="step"><span class="step__num">1</span><span class="step__text">This represents the comparisons of Completed Packets in CX vs Packet Tracking Gross Packets Received by Outreach</span></div>
    <div class="cell">Cell C4/27 "Call Center Reflects the number of Call Center Packets Completed</div>
    <div class="cell">Cell D4/27 "Complete Packets reflects the number of Packets completing the HIC Cycle for patient to become available for EPSDT Screenings</div>
    <div class="cell">Cell E4/27 "Duplicate Packets" defined as packets scanned that may have more than one packet scanned into CX</div>
    <div class="cell">Cell F4/27 "Incomplete Packets" is not scanned into CX, missing child history, located on the follow-up shelf for the call center to contact guardian</div>
    <div class="cell">Cell G4/27 "No signature" is define a packet without guardian signature, not scanned into CX and located on the follow-up shelf for the call center to contact guardian</div>
    <div class="cell">Cell H4/27 "declined Packet" guardian writes decline service on the packet and this packet is not scanned into CX</div>
    <div class="cell">Cell I4/27 "Blanks" is a completely blank packet and is not scanned into CX system</div>
    <div class="cell">Cell F5/28 "Total Packets = Call Center Packet + Complete Packets</div>
    <div class="cell">Cell G5/28 "Packet Tracking System" reflects the number estimated out of the Packet Tracking System, includes Call Center Packets +Complete Packets+ Duplicates Packets+ Incomplete Packets + No Signature + Declines + Blanks</div>
    <div class="cell">Cell J5/28 this represents the difference between the CX and Packet Tracking system Over/Under estimates</div>
    <div class="step"><span class="step__num">2</span><span class="step__text">Insured Packets step gives an forecast of how many insured EPSDT screening from the call center and completed packets minus the uninsured packets received</span></div>
    <div class="cell">Cell J8/J31 Uninsured packets cell contains exams completed with no insurance long with no insurance packets received</div>
    <div class="cell">Cell C31 (Call Center Packets) + D31 (Complete Packets) +F31 (Incomplete)+G31 (no signature) -Minus J31(uninsured) = Memphis</div>
    <div class="cell cell--italic">Memphis is calculated by adding back the incomplete and no signature packets per RLM</div>
    <div class="cell">Cell C8 (Call Center Packets) + D8(Complete Packets) -Minus J8 (uninsured) = NASH/KNOX</div>
    <div class="step"><span class="step__num">3</span><span class="step__text">Number of Completed exams for current School Year from billing report</span></div>
    <div class="step"><span class="step__num">4</span><span class="step__text">Left Behind/to Complete represents the number of available EPSDT screening to perform or unable to reach</span></div>
    <div class="step"><span class="step__num">5</span><span class="step__text">Comparison of Insured Packets 2017-18 vs. 2018-19</span></div>
    <div class="step"><span class="step__num">6</span><span class="step__text">Total gross packets received statewide = MEM + NASH</span></div>
    <div class="step"><span class="step__num">7</span><span class="step__text">Total Insured packets received statewide = MEM +NASH</span></div>
    <div class="step"><span class="step__num">8</span><span class="step__text">Statewide EPSDT Needs for Insured Packets = E16 + E32</span></div>
    <div class="step"><span class="step__num">9</span><span class="step__text">Gross Packet Needs to convert into Insured Packets @ 29% of Step 6</span></div>
  </div>
  <div class="page__footband"></div>
</section>

</body>
</html>
```